Business Card Design for a Sound engineer and DJ

We would like a residn of the business card.

Logo must remain the same.
The card is for the owner of the company.
The business card is in Arabic as the company is based in Kuwait.
The company specializes in sound engineering for singers concerts and events and in addition DJ.
The color options is up to the designer but we would like it masculine as the owner is a man.

Target Market(s)

All ages

Industry/Entity Type

Media

Contact Information for Business Card

Name:
Eng. Faisal Barrak
م/فيصل براك

The name above is in Arabic and English.

Title: General Manager
Mobile: +965 96370482
Office: +965 22480637
Email: info@qamarwave.net

Address:
Office no. 3
1st floor
Marjan Complex
Hamad Faraj St.
Salmiya
Kuwait

Instagram: @qamarwave
Snap: qamarwave

Requirements
Nice to have
• can we have Instagram icon and snap icon and a phone vector and email?
• Instead of writing the words

```html
<!DOCTYPE html>
<html lang="en">
<head>
<meta charset="utf-8">
<title>Qamar Wave – Business Card</title>
<link rel="stylesheet" href="https://fonts.googleapis.com/css2?family=Cairo:wght@500;700&family=Open+Sans:wght@400;600&family=Share+Tech+Mono&display=swap">
<style>
  :root {
    --bg: #e9e6e1;
    --card: #f7f7f7;
    --card-edge: #e4e4e6;
    --purple: #8e3fb0;
    --purple-dark: #7a2f9c;
    --violet-text: #7d4ab8;
    --blue-grey: #7f8fb8;
    --icon: #6f86c4;
    --ink-soft: #8a7aa8;
  }
  * { box-sizing: border-box; margin: 0; padding: 0; }
  html, body { width: 1200px; height: 780px; overflow: hidden; }
  body { background: var(--bg); position: relative; font-family: "Open Sans", sans-serif; }

  .card {
    position: absolute;
    background: linear-gradient(160deg, #ffffff 0%, var(--card) 55%, var(--card-edge) 100%);
    box-shadow: 0 10px 28px rgba(60, 50, 40, .25);
    overflow: hidden;
  }

  /* Front (portrait) */
  .card--front { left: 70px; top: 75px; width: 360px; height: 630px; }
  .card--front .brand { position: absolute; top: 92px; left: 0; right: 0; text-align: center; }
  .brand-name {
    font-family: "Share Tech Mono", monospace;
    color: var(--violet-text);
    letter-spacing: .22em;
    text-transform: uppercase;
  }
  .card--front .brand-name { font-size: 34px; }
  .tagline {
    font-family: "Share Tech Mono", monospace;
    color: var(--ink-soft);
    letter-spacing: .2em;
    font-size: 12px;
    margin-top: 10px;
  }
  .tagline-ar {
    font-family: "Cairo", sans-serif;
    color: var(--ink-soft);
    font-size: 13px;
    margin-top: 2px;
  }
  .person { position: absolute; top: 268px; left: 40px; right: 30px; }
  .person-name { font-size: 25px; font-weight: 600; color: var(--violet-text); }
  .person-name-ar { font-family: "Cairo", sans-serif; font-weight: 700; font-size: 17px; color: var(--purple); direction: rtl; text-align: left; }
  .person-title { font-size: 17px; color: var(--blue-grey); margin-top: 2px; }

  .contacts { position: absolute; top: 398px; left: 40px; list-style: none; }
  .contacts li { display: flex; align-items: center; gap: 10px; font-size: 17px; color: var(--violet-text); line-height: 27px; }
  .contacts svg { width: 17px; height: 17px; flex: none; }
  .socials { display: flex; gap: 26px; }
  .socials span { display: flex; align-items: center; gap: 8px; }
  .mark { width: 14px; height: 14px; background: var(--icon); border-radius: 3px; flex: none; }
  .mark--round { border-radius: 50%; }

  .band { position: absolute; background: linear-gradient(90deg, var(--purple-dark), var(--purple)); }
  .card--front .band { left: 0; right: 0; bottom: 0; height: 108px; }

  /* Back (landscape) */
  .card--back { left: 480px; top: 215px; width: 650px; height: 372px; }
  .card--back .brand { position: absolute; top: 92px; left: 0; right: 0; text-align: center; }
  .card--back .brand-name { font-size: 40px; }
  .card--back .band {
    left: 0; right: 0; bottom: 0; height: 66px;
    display: flex; align-items: center; justify-content: center;
    color: #fff; font-size: 16px; letter-spacing: .01em;
  }
</style>
</head>
<body>

<section class="card card--front" aria-label="Business card front">
  <div class="brand">
    <div class="brand-name">Qamar Wave</div>
    <div class="tagline">DJ - SOUND ENG. - LIGHTING</div>
    <div class="tagline-ar" dir="rtl">دي جي - هندسة صوت - إضاءة</div>
  </div>

  <div class="person">
    <div class="person-name">Eng. Faisal Barrak</div>
    <div class="person-name-ar">م/ فيصل براك</div>
    <div class="person-title">General Manager</div>
  </div>

  <ul class="contacts">
    <li>
      <svg viewBox="0 0 16 16" aria-hidden="true"><rect width="16" height="16" rx="3" fill="var(--icon)"/><rect x="5" y="2.5" width="6" height="11" rx="1.2" fill="#fff"/><rect x="6.2" y="4" width="3.6" height="6" fill="var(--icon)"/></svg>
      +965 96370482
    </li>
    <li>
      <svg viewBox="0 0 16 16" aria-hidden="true"><rect width="16" height="16" rx="3" fill="var(--icon)"/><path d="M4 5c1-1.5 2-1 2.5 0l.5 1.5-1 .8c.5 1.3 1.4 2.2 2.7 2.7l.8-1 1.5.5c1 .5 1.5 1.5 0 2.5C8 13 3 8 4 5z" fill="#fff"/></svg>
      +965 22480637
    </li>
    <li>
      <svg viewBox="0 0 16 16" aria-hidden="true"><rect width="16" height="16" rx="3" fill="var(--icon)"/><rect x="3" y="4.5" width="10" height="7" fill="#fff"/><path d="M3 4.5l5 4 5-4" fill="none" stroke="var(--icon)" stroke-width="1"/></svg>
      info@qamarwave.net
    </li>
    <li class="socials">
      <span><i class="mark" aria-hidden="true"></i>@qamarwave</span>
      <span><i class="mark mark--round" aria-hidden="true"></i>@qamarwave</span>
    </li>
  </ul>

  <div class="band"></div>
</section>

<section class="card card--back" aria-label="Business card back">
  <div class="brand">
    <div class="brand-name">Qamar Wave</div>
    <div class="tagline">DJ - SOUND ENG. - LIGHTING</div>
    <div class="tagline-ar" dir="rtl">دي جي - هندسة صوت - إضاءة</div>
  </div>
  <div class="band">Office no. 3, 1st floor, Marjan Complex, Hamad Faraj St., Salmiya, Kuwait</div>
</section>

</body>
</html>
```